PELDRAX Business Cards

We require a business card for our company that provides IT consulting services. We already have a logo that needs to be used on the card. We want a clean professional looking design that incorporates our colours. Our main focus is providing managed services to business, which involves us looking after all of their IT requirements including managing servers/networks, projects, and procurement.

Industry/Entity Type

Information Technology

Requirements
Must have
• our logo, contact information, name, title, phone numbers

```html
<!DOCTYPE html>
<html lang="en">
<head>
<meta charset="utf-8">
<title>PELDRAX Business Cards</title>
<link rel="stylesheet" href="https://fonts.googleapis.com/css2?family=Montserrat:wght@600&family=Roboto:wght@400;500&display=swap">
<style>
  :root {
    --brand-blue: #1ba1dc;
    --brand-deep: #0b4f8a;
    --brand-pale: #a6d5f2;
    --ink: #1c1c1c;
    --paper: #ffffff;
    --paper-shade: #c9c9c9;
    --stage: #161616;
  }
  * { margin: 0; padding: 0; box-sizing: border-box; }
  html, body { width: 1200px; height: 675px; overflow: hidden; background: var(--stage); }
  .sheet { position: relative; width: 1200px; height: 675px; }
  .card {
    position: absolute; top: 189px; width: 520px; height: 297px;
    background: var(--paper); overflow: hidden;
  }
  .card--front { left: 60px; }
  .card--back { left: 620px; }
  .card__art { position: absolute; inset: 0; }

  .wordmark {
    position: absolute; font-family: "Montserrat", sans-serif; font-weight: 600;
    color: var(--brand-blue); letter-spacing: 3px; line-height: 1;
  }
  .card--front .wordmark { left: 168px; top: 80px; font-size: 40px; }
  .card--back .wordmark {
    left: 0; right: 0; top: 124px; text-align: center; font-size: 52px;
    color: var(--paper); letter-spacing: 5px;
  }

  .holder { position: absolute; left: 168px; top: 140px; font-family: "Roboto", sans-serif; color: var(--ink); }
  .holder__name { font-size: 24px; font-weight: 500; letter-spacing: 0.3px; }
  .holder__title { font-size: 11px; margin-top: 2px; }

  .contact { position: absolute; left: 168px; top: 200px; list-style: none; font-family: "Roboto", sans-serif; font-size: 11px; color: var(--ink); }
  .contact__item { display: flex; align-items: center; gap: 8px; height: 22px; }
  .contact__icon { width: 12px; height: 12px; fill: var(--brand-blue); }
</style>
</head>
<body>
<main class="sheet">

  <section class="card card--front" aria-label="Card front">
    <svg class="card__art" viewBox="0 0 520 297" aria-hidden="true">
      <defs>
        <linearGradient id="topBand" x1="0" x2="1">
          <stop offset="0" stop-color="var(--brand-deep)"/>
          <stop offset="1" stop-color="var(--brand-pale)"/>
        </linearGradient>
      </defs>
      <rect x="150" y="0" width="370" height="62" fill="url(#topBand)"/>
      <rect x="0" y="0" width="150" height="297" fill="var(--brand-blue)"/>
      <rect x="0" y="70" width="150" height="60" fill="var(--paper)"/>
      <rect x="150" y="62" width="370" height="8" fill="var(--paper)"/>
      <polygon points="420,135 520,30 520,135" fill="var(--brand-blue)"/>
      <rect x="430" y="180" width="90" height="117" fill="var(--brand-blue)"/>
    </svg>

    <div class="wordmark">PELDRAX</div>

    <div class="holder">
      <p class="holder__name">Daniel Harwick</p>
      <p class="holder__title">President &amp; Technology Consultant</p>
    </div>

    <ul class="contact">
      <li class="contact__item">
        <svg class="contact__icon" viewBox="0 0 12 12"><path d="M6 0a4 4 0 0 0-4 4c0 3 4 8 4 8s4-5 4-8a4 4 0 0 0-4-4zm0 5.5A1.5 1.5 0 1 1 6 2.5a1.5 1.5 0 0 1 0 3z"/></svg>
        48 Ridge Road Box 902, Elm Falls, AB
      </li>
      <li class="contact__item">
        <svg class="contact__icon" viewBox="0 0 12 12"><path d="M2.5 0.5l2 2-1 1.5a7 7 0 0 0 4.5 4.5l1.5-1 2 2-1.5 2A10 10 0 0 1 0.5 2z"/></svg>
        403-555-0182
      </li>
      <li class="contact__item">
        <svg class="contact__icon" viewBox="0 0 12 12"><circle cx="6" cy="6" r="6"/></svg>
        https://peldrax.com
      </li>
    </ul>
  </section>

  <section class="card card--back" aria-label="Card back">
    <svg class="card__art" viewBox="0 0 520 297" aria-hidden="true">
      <defs>
        <linearGradient id="paperTop" x1="0" y1="0" x2="0" y2="1">
          <stop offset="0" stop-color="var(--paper-shade)"/>
          <stop offset="1" stop-color="var(--paper)"/>
        </linearGradient>
        <linearGradient id="paperBottom" x1="0" y1="0" x2="0" y2="1">
          <stop offset="0" stop-color="var(--paper)"/>
          <stop offset="1" stop-color="var(--paper-shade)"/>
        </linearGradient>
      </defs>
      <rect x="0" y="0" width="520" height="95" fill="url(#paperTop)"/>
      <rect x="0" y="95" width="520" height="112" fill="var(--brand-blue)"/>
      <rect x="0" y="207" width="520" height="90" fill="url(#paperBottom)"/>
    </svg>

    <div class="wordmark">PELDRAX</div>
  </section>

</main>
</body>
</html>
```